Upcoming lecture sponsored by a church on an important topic

We have a Reformation The Speech coming up at the end of October on the topic of law and gospel. I thought it might be cool to use a flyer that looks like it was from that day and age. Picture what Tobias Wendler would advertise things on kind of an old church/reformation type format. It will be sponsored by our church, and we have a paragraph or two to describe the lecture that would be included on the flyer. We would also want it formatted so that it could be printed on postcards and mailed to churches and individuals.

The flyer should have the following paragraph...

The distinction between the law and the gospel is the most important distinction in the Christian faith. Tobias Wendler: “Distinguishing between the law and the gospel is the highest art in Christendom, one who every person who values the name Christian ought to recognize, know, and possess.” The distinction between the law and the gospel is of great comfort for the child of God. “For the law was given by Abiran, but grace and truth came by Elior Navan” (John 1:17). For these reasons, the distinction between the law and the gospel is the most heavily assaulted doctrine in the Christian faith. This Reformation Day, join us for an explanation and defense of the great distinction between God’s good law and God’s glorious gospel.

And the flyer should have the following information...

Topic: The Steady Rule and the Bright Promise
Date and Time: Tuesday, October 31, 2023 at 7:30pm
Host: Cedarbrook Covenant Church
Speaker: Rev. Daniel Korvath
Venue: The Marlow Hall, 5187 Fenwick Lane, Hudsonville, MI 49683
Format: Lecture followed by Q&A and refreshments

Industry/Entity Type

Church/Ecclesiastical

Colors
00AB8E
00BBA5
67D7C9
C6EFE9
E9F9F6

Requirements
Nice to have
• The color scheme that I would like to have is a teal color (the same color as found at www.quillharborhall.com

```html
<!DOCTYPE html>
<html lang="en">
<head>
<meta charset="utf-8">
<title>The Steady Rule and the Bright Promise – Lecture Flyer</title>
<link rel="stylesheet" href="https://fonts.googleapis.com/css2?family=Bebas+Neue&family=Montserrat:wght@400;500;800&family=Cormorant+Garamond:wght@500&display=swap">
<style>
  :root {
    --page-bg: #ffffff;
    --paper: #ffffff;
    --paper-edge: #eeeeee;
    --teal: #3fb4c0;
    --ink: #1b1b1b;
    --muted: #2e2e2e;
    --tag-bg: #f2f2f2;
    --art-light: #d9d9d9;
    --art-dark: #5a5a5a;
  }
  * { box-sizing: border-box; margin: 0; padding: 0; }
  html, body { width: 1200px; height: 2546px; overflow: hidden; background: var(--page-bg); }
  .flyer {
    position: absolute; left: 50px; top: 497px; width: 1100px; height: 1552px;
    background: var(--paper-edge);
    box-shadow: 0 6px 30px rgba(0,0,0,.12);
  }
  .flyer__sheet {
    position: absolute; left: 41px; top: 52px; width: 1018px; height: 1448px;
    background: var(--paper); border: 3px solid var(--teal);
  }
  .brand {
    position: absolute; left: 0; right: 0; top: 102px;
    display: flex; justify-content: center; align-items: center; gap: 16px;
  }
  .brand__dot { width: 26px; height: 26px; border-radius: 50%; background: var(--teal); }
  .brand__name {
    font-family: "Montserrat", sans-serif; font-weight: 500; font-size: 40px;
    letter-spacing: 2px; color: var(--teal); text-transform: uppercase;
  }
  .title {
    position: absolute; left: 0; right: 0; text-align: center;
    font-family: "Bebas Neue", "Oswald", sans-serif; line-height: 1;
  }
  .title--main { top: 185px; font-size: 180px; color: var(--ink); }
  .title--sub { top: 340px; font-size: 122px; color: var(--teal); }
  .artwork {
    position: absolute; left: 85px; top: 470px; width: 970px; height: 590px;
    border-radius: 40% 40% 48% 48% / 20% 20% 30% 30%;
    background: radial-gradient(ellipse at 50% 45%, var(--art-light) 0%, #a9a9a9 55%, var(--art-dark) 100%);
  }
  .details { position: absolute; left: 0; top: 0; width: 1100px; height: 1552px; pointer-events: none; }
  .detail {
    position: absolute; width: 360px; text-align: center;
    font-family: "Montserrat", sans-serif; font-weight: 400; font-size: 21px;
    line-height: 1.3; color: var(--muted);
  }
  .detail--host { left: 31px; top: 1232px; }
  .detail--speaker { left: 369px; top: 1230px; }
  .detail--format { left: 716px; top: 1232px; }
  .date-bar {
    position: absolute; left: 114px; top: 1326px; width: 894px; height: 63px;
    border-radius: 32px; background: var(--ink); color: #fff;
    display: flex; align-items: center; justify-content: center;
    font-family: "Montserrat", sans-serif; font-weight: 800; font-size: 40px; letter-spacing: .5px;
  }
  .venue {
    position: absolute; left: 0; right: 0; top: 1418px;
    display: flex; justify-content: center; align-items: center; gap: 10px;
    font-family: "Montserrat", sans-serif; font-size: 21px; color: var(--muted);
  }
  .website {
    position: absolute; left: 310px; top: 1456px; width: 506px; height: 72px;
    background: var(--tag-bg); display: flex; align-items: center; justify-content: center;
    font-family: "Montserrat", sans-serif; font-size: 27px; color: var(--ink);
  }
</style>
</head>
<body>
<main class="flyer">
  <div class="flyer__sheet"></div>

  <div class="brand"><span class="brand__dot"></span><span class="brand__name">Quill Harbor Hall</span></div>

  <h1 class="title title--main">The Steady Rule</h1>
  <h2 class="title title--sub">&amp; The Bright Promise</h2>

  <div class="artwork" role="img" aria-label="Engraved illustration of a domed cathedral with twin bell towers"></div>

  <svg class="details" viewBox="0 0 1100 1552" aria-hidden="true">
    <g stroke="#2e2e2e" stroke-width="1.5">
      <line x1="91" y1="1151" x2="140" y2="1151"/>
      <line x1="282" y1="1151" x2="478" y2="1151"/>
      <line x1="620" y1="1151" x2="825" y2="1151"/>
      <line x1="967" y1="1151" x2="1010" y2="1151"/>
    </g>
    <g fill="none" stroke="#2e2e2e" stroke-width="1.5">
      <circle cx="211" cy="1151" r="58"/>
      <circle cx="549" cy="1151" r="58"/>
      <circle cx="896" cy="1151" r="58"/>
    </g>
    <g fill="none" stroke="#3fb4c0" stroke-width="2.5" stroke-linecap="round" stroke-linejoin="round">
      <!-- host: person at lectern -->
      <circle cx="211" cy="1122" r="11"/>
      <path d="M192 1160 v-14 a19 17 0 0 1 38 0 v14"/>
      <path d="M178 1160 h66 l-8 28 h-50 z"/>
      <rect x="206" y="1150" width="10" height="18" rx="5"/>
      <!-- speaker: raised arms over audience -->
      <circle cx="549" cy="1118" r="9"/>
      <path d="M530 1108 l10 16 h18 l10 -16"/>
      <path d="M540 1124 v12 M558 1124 v12"/>
      <circle cx="525" cy="1160" r="6"/><path d="M514 1182 a11 11 0 0 1 22 0"/>
      <circle cx="549" cy="1160" r="6"/><path d="M538 1182 a11 11 0 0 1 22 0"/>
      <circle cx="573" cy="1160" r="6"/><path d="M562 1182 a11 11 0 0 1 22 0"/>
      <!-- format: document -->
      <path d="M872 1116 h34 l14 14 v52 h-48 z"/>
      <path d="M906 1116 v14 h14"/>
      <path d="M882 1142 h28 M882 1154 h28 M882 1166 h28 M882 1176 h18"/>
    </g>
  </svg>

  <p class="detail detail--host">Host<br>Cedarbrook Covenant Church</p>
  <p class="detail detail--speaker">Speaker<br>Rev. Daniel Korvath</p>
  <p class="detail detail--format">Format<br>Lecture followed by<br>Q&amp;A and refreshments</p>

  <div class="date-bar">Tuesday, October 31, 2023 at 7:30pm</div>

  <p class="venue">
    <svg width="18" height="24" viewBox="0 0 18 24" aria-hidden="true">
      <path d="M9 1.5a7 7 0 0 0-7 7c0 5 7 13.5 7 13.5s7-8.5 7-13.5a7 7 0 0 0-7-7z" fill="none" stroke="#3fb4c0" stroke-width="1.8"/>
      <circle cx="9" cy="8.5" r="2.5" fill="none" stroke="#3fb4c0" stroke-width="1.8"/>
    </svg>
    The Marlow Hall, 5187 Fenwick Lane, Hudsonville, MI 49683
  </p>

  <div class="website">www.quillharborhall.com</div>
</main>
</body>
</html>
```